Book Cover

Book cover for a study guide on Galatians. The title would be: "Corvenites: Lifted Up to Stand Tall" Possibly using a bird breaking free from a cage.+

Target Market(s)

We will sell them to our church.

Requirements
Must have
• Authors are Dr. Martin Korvel and Dr. Helen Korvel

```html
<!DOCTYPE html>
<html lang="en">
<head>
<meta charset="utf-8">
<title>Corvenites: Lifted Up to Stand Tall — Book Cover</title>
<link rel="stylesheet" href="https://fonts.googleapis.com/css2?family=Oswald:wght@600;700&family=Libre+Caslon+Text:wght@400&family=Great+Vibes&display=swap">
<style>
  :root {
    --page-bg: #ececec;
    --cream: #efe6d4;
    --sky-glow: #e9b24a;
    --sky-mid: #b77a2a;
    --sky-deep: #5a3515;
    --sky-edge: #1f1108;
    --cage-light: #c98a2e;
    --cage-mid: #8a5220;
    --cage-dark: #4a2810;
    --cover-shadow: rgba(0, 0, 0, 0.28);
  }
  * { margin: 0; padding: 0; box-sizing: border-box; }
  html, body {
    width: 1200px;
    height: 1200px;
    overflow: hidden;
    background: var(--page-bg);
  }
  .cover {
    position: absolute;
    left: 230px;
    top: 45px;
    width: 740px;
    height: 1110px;
    overflow: hidden;
    box-shadow: 0 18px 40px var(--cover-shadow);
  }
  .cover-sky {
    position: absolute;
    inset: 0;
    background:
      radial-gradient(ellipse 70% 55% at 50% 50%, var(--sky-glow) 0%, var(--sky-mid) 45%, var(--sky-deep) 80%, var(--sky-edge) 100%);
  }
  .cover-sky::after {
    content: "";
    position: absolute;
    left: 0; right: 0; bottom: 0;
    height: 220px;
    background: linear-gradient(to bottom, rgba(31,17,8,0) 0%, rgba(31,17,8,0.85) 70%, var(--sky-edge) 100%);
  }
  .cage-illustration {
    position: absolute;
    left: 205px;
    top: 395px;
    width: 330px;
    height: 640px;
    border-radius: 165px 165px 14px 14px;
    background:
      radial-gradient(ellipse 60% 45% at 50% 40%, var(--cage-light) 0%, var(--cage-mid) 60%, var(--cage-dark) 100%);
    opacity: 0.9;
  }
  .book-title {
    position: absolute;
    top: 42px;
    left: 0;
    width: 100%;
    text-align: center;
    font-family: "Oswald", sans-serif;
    font-weight: 700;
    font-size: 124px;
    line-height: 1;
    letter-spacing: -1px;
    color: var(--cream);
    text-transform: uppercase;
  }
  .subtitle {
    position: absolute;
    top: 205px;
    left: 0;
    width: 100%;
    height: 220px;
    color: var(--cream);
  }
  .subtitle-stack {
    position: absolute;
    left: 175px;
    top: 0;
    width: 260px;
    text-align: center;
    font-family: "Libre Caslon Text", serif;
    line-height: 1.02;
  }
  .subtitle-stack .line-lg { display: block; font-size: 58px; }
  .subtitle-stack .line-sm { display: block; font-size: 44px; }
  .subtitle-script {
    position: absolute;
    left: 400px;
    top: 40px;
    font-family: "Great Vibes", cursive;
    font-size: 150px;
    line-height: 1;
  }
  .authors {
    position: absolute;
    bottom: 48px;
    left: 0;
    width: 100%;
    text-align: center;
    font-family: "Oswald", sans-serif;
    font-weight: 600;
    font-size: 38px;
    letter-spacing: 0.5px;
    color: var(--cream);
    text-transform: uppercase;
  }
</style>
</head>
<body>
  <main class="cover">
    <div class="cover-sky" role="img" aria-label="Glowing golden sunset sky with dark birds flying freely across it"></div>
    <div class="cage-illustration" role="img" aria-label="Illustration of an ornate domed birdcage standing open in the centre of the cover"></div>
    <h1 class="book-title">Corvenites</h1>
    <p class="subtitle">
      <span class="subtitle-stack">
        <span class="line-lg">Lifted Up</span>
        <span class="line-sm">to</span>
        <span class="line-lg">Stand</span>
      </span>
      <span class="subtitle-script">Tall</span>
    </p>
    <p class="authors">Dr. Martin Korvel &amp; Dr. Helen Korvel</p>
  </main>
</body>
</html>
```